Coaching and Tutoring that removes all obstacles and leads to success and happiness

Tutoring maths giving confidence, clarity and success to students of all abilities. Tutoring from 14 years to 18 years old. Dealing with exam preparation and stress.
Coaching confidence, resilience and ultimately happiness and freedom.
The design to inspire and reassure people of a safe pair of hands as well excitement of the beginning of something new in their lives.

Target Market(s)

20 -30 year olds

Industry/Entity Type

Self Development and Education

Contact Information for Business Card

Confidence Coach and Maths Tutor

Font styles to use
Sans Serif

Colors
EE7325
F08F49
F5BC92
FAE3D3
FDF4ED

Requirements
Must have
• Success and Happiness

```html
<!DOCTYPE html>
<html lang="en">
<head>
<meta charset="utf-8">
<title>Maple Brook Coaching – Business Card</title>
<link rel="stylesheet" href="https://fonts.googleapis.com/css2?family=Lato:wght@400;700&family=Cinzel:wght@500&family=Archivo+Black&display=swap">
<style>
  :root {
    --green: #8ab43a;
    --green-dark: #7aa32f;
    --orange: #ee7325;
    --ink: #1d1d1d;
    --white: #ffffff;
    --backdrop: #ece8e3;
    --sky-light: #f4efe1;
    --sky: #9fb0c2;
    --hedge: #2a3122;
    --grass: #3f5a27;
  }
  * { margin: 0; padding: 0; box-sizing: border-box; }
  html, body { width: 1200px; height: 900px; overflow: hidden; }
  body {
    background: var(--backdrop);
    font-family: "Lato", sans-serif;
    position: relative;
  }
  .card {
    position: absolute;
    left: 290px;
    width: 620px;
    height: 354px;
    overflow: hidden;
    box-shadow: 0 10px 26px rgba(0,0,0,0.18);
  }
  .card--front { top: 76px; }
  .card--back { top: 470px; background: var(--white); }

  /* Front */
  .front-photo {
    position: absolute; inset: 0;
    background:
      radial-gradient(ellipse 140px 110px at 52% 30%, var(--sky-light) 0%, rgba(244,239,225,0.6) 45%, rgba(244,239,225,0) 100%),
      linear-gradient(180deg, var(--sky) 0%, #c9c9c4 32%, #5d6152 55%, var(--hedge) 75%, var(--grass) 100%);
  }
  .brand {
    position: absolute;
    display: flex; align-items: center; gap: 10px;
    color: var(--green);
    font-family: "Lato", sans-serif;
    font-weight: 700;
    letter-spacing: 0.12em;
    text-transform: uppercase;
    white-space: nowrap;
  }
  .brand__dot {
    border-radius: 50%;
    background: var(--orange);
    flex: none;
  }
  .card--front .brand { top: 44px; left: 50%; transform: translateX(-50%); font-size: 26px; }
  .card--front .brand__dot { width: 30px; height: 30px; }
  .tagline {
    position: absolute;
    bottom: 40px; left: 0; right: 0;
    text-align: center;
    font-family: "Archivo Black", sans-serif;
    font-size: 34px;
    color: var(--green);
    letter-spacing: 0.01em;
  }

  /* Back */
  .back-wave { position: absolute; inset: 0; width: 100%; height: 100%; }
  .person { position: absolute; top: 44px; left: 40px; }
  .person__name {
    font-family: "Cinzel", serif;
    font-weight: 500;
    font-size: 24px;
    color: var(--green);
    letter-spacing: 0.04em;
    line-height: 1;
  }
  .person__role { font-size: 15px; color: var(--ink); margin-top: 2px; }
  .contact { position: absolute; top: 142px; left: 40px; font-size: 15px; color: var(--ink); line-height: 1.4; }
  .contact__row { display: flex; align-items: center; gap: 10px; }
  .contact__icon { width: 18px; height: 18px; flex: none; }
  .contact__address { margin-top: 16px; padding-left: 28px; }
  .card--back .brand { top: 96px; right: 36px; font-size: 24px; }
  .card--back .brand__dot { width: 26px; height: 26px; }
  .website {
    position: absolute; right: 40px; bottom: 40px;
    color: var(--white); font-size: 14px; letter-spacing: 0.02em;
  }
</style>
</head>
<body>

  <section class="card card--front">
    <div class="front-photo" role="img" aria-label="Photograph of a person walking through a wooden gate on a sunlit countryside path between bare trees and hedges"></div>
    <div class="brand"><span class="brand__dot"></span>Maple Brook Coaching</div>
    <p class="tagline">SUCCESS AND HAPPINESS</p>
  </section>

  <section class="card card--back">
    <svg class="back-wave" viewBox="0 0 620 354" preserveAspectRatio="none" aria-hidden="true">
      <path d="M0,262 C200,268 350,240 470,180 C380,250 220,282 0,284 Z" fill="var(--orange)"/>
      <path d="M0,290 C210,292 380,250 520,180 C560,162 595,152 620,148 L620,354 L0,354 Z" fill="var(--green)"/>
    </svg>

    <div class="person">
      <h1 class="person__name">DANIEL REEVE</h1>
      <p class="person__role">Confidence Coach and Maths Tutor</p>
    </div>

    <div class="contact">
      <div class="contact__row">
        <svg class="contact__icon" viewBox="0 0 24 24" aria-hidden="true"><path fill="var(--green)" d="M6.6 10.8c1.4 2.8 3.8 5.1 6.6 6.6l2.2-2.2c.3-.3.7-.4 1-.2 1.1.4 2.3.6 3.6.6.6 0 1 .4 1 1V20c0 .6-.4 1-1 1C10.6 21 3 13.4 3 4c0-.6.4-1 1-1h3.5c.6 0 1 .4 1 1 0 1.3.2 2.5.6 3.6.1.3 0 .7-.2 1z"/></svg>
        <span>044-555 010 247</span>
      </div>
      <div class="contact__row">
        <svg class="contact__icon" viewBox="0 0 24 24" aria-hidden="true"><rect x="2" y="5" width="20" height="14" fill="var(--green)"/><path d="M2 5l10 8 10-8" fill="none" stroke="var(--white)" stroke-width="1.6"/></svg>
        <span>hello@maplebrook.com</span>
      </div>
      <p class="contact__address">18 Orchard Lane, Hillside<br>Westvale, 30417</p>
    </div>

    <div class="brand"><span class="brand__dot"></span>Maple Brook Coaching</div>

    <p class="website">www.maplebrookcoach.com</p>
  </section>

</body>
</html>
```